International Food Company needs packaging design for new products

We have a logo for our new business. It is attached. Now we need a packaging design for the products that we will be selling. We are an international wholesale foods company selling foods and herbs that will be certified organic and Non-GMO imported from West Africa. We are just in the process of launching new products. We're looking for a design that is fresh and modern.

Here is a list of items that we are requesting packaging design for.

Baobob Powder-8 oz and 12 oz
Dried Mango- 8 oz
Mango Powder 8 oz and 12 oz

```html
<!DOCTYPE html>
<html lang="en">
<head>
<meta charset="UTF-8">
<title>Kora Harvest – Product Pouches</title>
<link href="https://fonts.googleapis.com/css2?family=Bree+Serif&family=Raleway:wght@400;600&display=swap" rel="stylesheet">
<style>
  :root {
    --bg: #fcf1f0;
    --pouch: #ffffff;
    --seal: #f1f1f1;
    --title: #2f5a24;
    --green: #7dc142;
    --green-dark: #5ea52b;
    --orange: #f0892a;
    --orange-dark: #d9701a;
    --badge-line: rgba(255,255,255,0.9);
  }
  * { margin: 0; padding: 0; box-sizing: border-box; }
  html, body { width: 1200px; height: 849px; overflow: hidden; }
  body {
    background: var(--bg);
    font-family: "Raleway", sans-serif;
  }
  .range {
    position: relative;
    width: 1200px;
    height: 849px;
    display: flex;
    justify-content: center;
    align-items: center;
    gap: 92px;
  }
  .pouch {
    position: relative;
    width: 266px;
    height: 464px;
    background: var(--pouch);
    border-radius: 10px 10px 6px 6px;
    box-shadow: 0 10px 24px rgba(120, 80, 70, 0.12);
    overflow: hidden;
  }
  .pouch__seal {
    position: absolute;
    top: 0; left: 0; right: 0;
    height: 36px;
    background: var(--seal);
    border-bottom: 1px solid #e4e4e4;
  }
  .brand {
    position: absolute;
    top: 76px; left: 0; right: 0;
    display: flex;
    justify-content: center;
    align-items: center;
    gap: 7px;
  }
  .brand__dot {
    width: 9px; height: 9px;
    border-radius: 50%;
    background: var(--title);
  }
  .brand__name {
    font-family: "Bree Serif", serif;
    font-size: 16px;
    color: var(--title);
    line-height: 1;
  }
  .product-title {
    position: absolute;
    top: 150px; left: 0; right: 0;
    font-family: "Bree Serif", serif;
    font-weight: 400;
    font-size: 42px;
    line-height: 1.08;
    letter-spacing: 1px;
    color: var(--title);
    text-align: center;
    text-transform: uppercase;
  }
  .product-title::after {
    content: "";
    display: block;
    width: 150px;
    height: 2px;
    margin: 8px auto 0;
    background: var(--title);
  }
  .pouch__band {
    position: absolute;
    left: 0; bottom: 0;
    width: 100%;
    height: 200px;
  }
  .product-photo {
    position: absolute;
    left: 50%;
    top: 276px;
    width: 150px;
    height: 110px;
    transform: translateX(-50%);
    border-radius: 50%;
  }
  .product-photo--mango-powder { background: radial-gradient(circle at 45% 45%, #f8c94a, #f0a92c 65%, rgba(240,169,44,0) 72%); }
  .product-photo--dried-mango { background: radial-gradient(circle at 50% 50%, #f4c230, #e8a020 60%, rgba(130,170,50,0.9) 70%, rgba(130,170,50,0) 74%); }
  .product-photo--baobab { background: radial-gradient(circle at 45% 45%, #f3e3c2, #d8bf95 60%, rgba(150,110,90,0.8) 68%, rgba(150,110,90,0) 74%); }
  .net-weight {
    position: absolute;
    left: 14px; bottom: 58px;
    width: 28px; height: 28px;
    border-radius: 50%;
    background: rgba(0,0,0,0.18);
    color: #fff;
    font-size: 8px;
    font-weight: 600;
    display: flex; align-items: center; justify-content: center;
  }
  .claims {
    position: absolute;
    right: 14px; bottom: 44px;
    display: flex;
    gap: 10px;
  }
  .claim {
    display: flex; flex-direction: column; align-items: center; gap: 3px;
    font-size: 6px;
    color: #fff;
  }
  .claim__badge {
    width: 24px; height: 24px;
    border-radius: 50%;
    border: 1.5px solid var(--badge-line);
  }
</style>
</head>
<body>
<main class="range">

  <article class="pouch">
    <div class="pouch__seal"></div>
    <div class="brand"><span class="brand__dot"></span><p class="brand__name">Kora Harvest</p></div>
    <h1 class="product-title">Mango<br>Powder</h1>
    <svg class="pouch__band" viewBox="0 0 266 200" preserveAspectRatio="none">
      <path d="M0 70 Q133 30 266 70 L266 200 L0 200 Z" fill="var(--green)"/>
      <path d="M0 190 L266 190 L266 200 L0 200 Z" fill="var(--green-dark)"/>
    </svg>
    <div class="product-photo product-photo--mango-powder" role="img" aria-label="Heap of mango powder with fresh cut mango"></div>
    <span class="net-weight">8 oz</span>
    <div class="claims">
      <div class="claim"><span class="claim__badge"></span>Non GMO</div>
      <div class="claim"><span class="claim__badge"></span>Organic</div>
    </div>
  </article>

  <article class="pouch">
    <div class="pouch__seal"></div>
    <div class="brand"><span class="brand__dot"></span><p class="brand__name">Kora Harvest</p></div>
    <h1 class="product-title">Dried<br>Mango</h1>
    <svg class="pouch__band" viewBox="0 0 266 200" preserveAspectRatio="none">
      <path d="M0 70 Q133 30 266 70 L266 200 L0 200 Z" fill="var(--orange)"/>
      <path d="M0 190 L266 190 L266 200 L0 200 Z" fill="var(--orange-dark)"/>
    </svg>
    <div class="product-photo product-photo--dried-mango" role="img" aria-label="Dried mango slices with a whole green mango"></div>
    <span class="net-weight">8 oz</span>
    <div class="claims">
      <div class="claim"><span class="claim__badge"></span>Non GMO</div>
      <div class="claim"><span class="claim__badge"></span>Organic</div>
    </div>
  </article>

  <article class="pouch">
    <div class="pouch__seal"></div>
    <div class="brand"><span class="brand__dot"></span><p class="brand__name">Kora Harvest</p></div>
    <h1 class="product-title">Baobab<br>Powder</h1>
    <svg class="pouch__band" viewBox="0 0 266 200" preserveAspectRatio="none">
      <path d="M0 70 Q133 30 266 70 L266 200 L0 200 Z" fill="var(--green)"/>
      <path d="M0 190 L266 190 L266 200 L0 200 Z" fill="var(--green-dark)"/>
    </svg>
    <div class="product-photo product-photo--baobab" role="img" aria-label="Heap of baobab powder beside an open baobab fruit pod"></div>
    <span class="net-weight">8 oz</span>
    <div class="claims">
      <div class="claim"><span class="claim__badge"></span>Non GMO</div>
      <div class="claim"><span class="claim__badge"></span>Organic</div>
    </div>
  </article>

</main>
</body>
</html>
```